Pastry Trade Institute Website Homepage Revision

I need the "homepage" to the new Northfield Pastry Trade Institute to reworked. The current homepage is dull. It needs the attention of a professional graphic artist so it delivers a professionally finished feel and look. I have included the current URL for your viewing (builds.vorlimo.com/bridal-torte/cms/ ) to see where we are in the development phase. The elements on the homepage are all necessary and the colors are correct. I have also included the original Word document for the page (you can extract the RGB values and images from the doc). To be clear, I am not looking to recreate all the web pages, just the homepage. It needs to be responsive and stretched.

Target Market(s)

All bakers who sell wedding cakes in the United States

Number of Pages Required

1 page

Font styles to use
Other font styles liked:
• see the Word Document

Requirements
Must have
• It must have the elements already in the original mock up. That includes the colors and fonts.

```html
<!DOCTYPE html>
<html lang="en">
<head>
<meta charset="utf-8">
<title>Northfield Pastry Trade Institute – Home</title>
<link rel="stylesheet" href="https://fonts.googleapis.com/css2?family=Raleway:wght@400;500;600;700;800&display=swap">
<style>
  :root {
    --rose: #c8566a;
    --rose-deep: #b8475b;
    --rose-light: #f1d3d8;
    --rose-pale: #f8e8eb;
    --cream: #e9e5d7;
    --grey: #7b7b7b;
    --grey-light: #e8e8e8;
    --ink: #3a3a3a;
    --text: #555;
    --footer: #2a2a2a;
    --white: #fff;
  }
  * { box-sizing: border-box; margin: 0; padding: 0; }
  html, body { width: 1200px; height: 2990px; overflow: hidden; }
  body { position: relative; background: var(--white); font-family: "Raleway", sans-serif; color: var(--text); }
  .abs { position: absolute; }

  /* header */
  .brand { left: 238px; top: 8px; width: 120px; height: 56px; display: flex; align-items: center; gap: 8px; }
  .brand-dot { width: 14px; height: 14px; border-radius: 50%; background: var(--rose); flex: none; }
  .brand-name { font-size: 11px; font-weight: 600; color: var(--rose); line-height: 1.2; }
  .member-login { left: 848px; top: 24px; width: 112px; height: 26px; border-radius: 13px; background: var(--grey); color: var(--white); font-size: 11px; font-weight: 700; display: flex; align-items: center; justify-content: center; }
  .main-nav { left: 0; top: 72px; width: 1200px; height: 30px; background: var(--rose); display: flex; justify-content: space-between; align-items: center; padding: 0 238px 0 242px; }
  .main-nav a { color: var(--white); font-size: 10.5px; font-weight: 800; text-decoration: none; letter-spacing: .2px; }

  /* hero */
  .hero-photo { left: 0; top: 102px; width: 1200px; height: 680px; background: radial-gradient(ellipse at 30% 45%, #f2e6e4 0%, #d8aeb4 35%, #a86677 70%, #8a4d5d 100%); }
  .hero-wave { left: 0; top: 650px; width: 1200px; height: 140px; }
  .signup-card { left: 716px; top: 248px; width: 244px; height: 334px; background: var(--grey-light); padding: 18px 16px; }
  .signup-card h3 { font-size: 11px; color: var(--rose); font-weight: 700; margin-bottom: 18px; }
  .signup-card .flower { position: absolute; right: 0; top: 0; width: 52px; height: 44px; background: radial-gradient(circle, #e9a7b6, #e8e8e8 70%); }
  .signup-card label { display: block; font-size: 9.5px; color: var(--ink); margin-bottom: 4px; }
  .signup-card .field { height: 22px; border: 2px solid #444; background: #ddd; font-size: 8px; color: #888; padding: 4px 8px; margin-bottom: 12px; }
  .btn { display: flex; align-items: center; justify-content: center; border-radius: 12px; color: var(--white); font-size: 9.5px; font-weight: 700; height: 24px; }
  .btn-rose { background: var(--rose); }
  .btn-grey { background: var(--grey); }
  .signup-card .btn { width: 112px; margin: 10px auto 0; }

  /* press */
  .press { left: 246px; top: 784px; width: 714px; height: 52px; display: flex; justify-content: space-between; align-items: center; }
  .press span { width: 52px; height: 40px; background: #c9c9c9; border-radius: 4px; }
  .press span:nth-child(4) { border-radius: 50%; width: 42px; height: 42px; }

  /* video */
  .video { left: 244px; top: 872px; width: 430px; height: 264px; background: linear-gradient(135deg, #d97a8c, #c65a6e); }
  .video-title { position: absolute; left: 0; right: 0; top: 100px; text-align: center; color: var(--white); font-size: 12px; font-weight: 700; }
  .video-play { position: absolute; left: 188px; top: 120px; width: 52px; height: 52px; }
  .video-bar { position: absolute; left: 0; bottom: 0; width: 100%; height: 20px; background: #2a2a2a; }
  .video-bar i { position: absolute; left: 38px; top: 9px; width: 200px; height: 2px; background: #888; }
  .video-bar b { position: absolute; left: 38px; top: 9px; width: 66px; height: 2px; background: var(--white); }
  .discover { left: 712px; top: 872px; width: 246px; height: 264px; background: var(--grey-light); padding: 18px 22px; text-align: center; }
  .discover h3 { font-size: 15px; font-weight: 500; color: var(--ink); line-height: 1.3; margin-bottom: 14px; }
  .input { height: 26px; background: var(--white); font-size: 9px; color: #aaa; text-align: left; padding: 7px 10px; margin-bottom: 10px; }
  .discover .btn { width: 112px; margin: 4px auto 0; }

  /* florals */
  .floral-right { left: 1060px; top: 900px; width: 140px; height: 540px; background: radial-gradient(ellipse at 70% 50%, #f3d3da 0%, #f6e6e8 45%, rgba(255,255,255,0) 75%); }
  .floral-left { left: 0; top: 1170px; width: 130px; height: 610px; background: radial-gradient(ellipse at 20% 50%, #f3d3da 0%, #f6e6e8 45%, rgba(255,255,255,0) 75%); }

  /* sections */
  .section-title { left: 0; width: 1200px; text-align: center; color: var(--rose); font-size: 22px; font-weight: 700; }
  .section-sub { left: 0; width: 1200px; text-align: center; font-size: 11px; color: var(--text); }
  .market-cards { left: 244px; top: 1276px; width: 716px; display: flex; justify-content: space-between; }
  .market-card { width: 166px; height: 128px; background: var(--cream); text-align: center; padding: 26px 12px 0; }
  .market-card p { font-size: 12px; font-weight: 700; color: var(--ink); line-height: 1.3; height: 44px; }
  .market-card .btn { width: 80px; margin: 10px auto 0; }
  .sales-cards { left: 244px; top: 1546px; width: 716px; display: flex; justify-content: space-between; }
  .sales-card { width: 224px; height: 264px; background: var(--rose-pale); text-align: center; }
  .sales-card .photo { height: 148px; border: 5px solid var(--rose); }
  .sales-card p { font-size: 10px; color: var(--ink); line-height: 1.4; padding: 12px 16px 0; height: 74px; }
  .sales-card .btn { width: 112px; margin: 0 auto; }

  /* founder */
  .founder-band { left: 0; top: 1830px; width: 1200px; height: 512px; }
  .founder-photo { left: 244px; top: 1990px; width: 242px; height: 286px; background: linear-gradient(160deg, #f3eee8, #d9b9a5 55%, #6a6a6a); overflow: hidden; }
  .founder-ribbon { position: absolute; right: -34px; top: 18px; width: 140px; height: 22px; background: var(--rose); color: var(--white); font-size: 10px; font-weight: 700; transform: rotate(45deg); text-align: center; line-height: 22px; }
  .founder-copy { left: 538px; top: 2016px; width: 424px; color: var(--ink); }
  .founder-copy h2 { font-size: 14px; font-weight: 700; line-height: 1.35; margin-bottom: 12px; }
  .founder-copy p { font-size: 11px; line-height: 1.5; margin-bottom: 12px; }

  /* advisory */
  .advisory-copy { left: 244px; top: 2412px; width: 440px; color: var(--grey); font-size: 15px; font-weight: 700; line-height: 1.4; }
  .advisory-copy p { margin-bottom: 20px; }
  .advisory-copy em { font-style: normal; color: var(--rose); }
  .advisory-form { left: 712px; top: 2404px; width: 246px; height: 246px; background: var(--white); box-shadow: 0 2px 10px rgba(0,0,0,.15); padding: 14px 24px; text-align: center; }
  .advisory-form .input { border: 1px solid #bbb; height: 24px; padding: 6px 10px; }
  .advisory-form .btn { width: 112px; margin: 6px auto 10px; }
  .advisory-form small { display: block; font-size: 9.5px; color: var(--ink); line-height: 1.4; }

  /* footer */
  .site-footer { left: 0; top: 2714px; width: 1200px; height: 276px; background: var(--footer); }
  .footer-col { position: absolute; top: 56px; }
  .footer-col h4 { font-size: 11px; font-weight: 700; color: var(--rose); margin-bottom: 16px; }
  .footer-col li { list-style: none; font-size: 10px; font-weight: 600; color: var(--white); line-height: 1.4; }
  .copyright { position: absolute; left: 0; width: 100%; top: 214px; text-align: center; font-size: 9.5px; color: #999; }
</style>
</head>
<body>

<header>
  <div class="abs brand"><span class="brand-dot"></span><span class="brand-name">Northfield Pastry Trade Institute</span></div>
  <div class="abs member-login">MEMBER LOGIN</div>
  <nav class="abs main-nav">
    <a>HOME</a><a>RAY'S STORY</a><a>MARKETING SOLUTIONS</a><a>SALES SOLUTIONS</a><a>HIRE US</a><a>CONTACT</a><a>PARTNER WITH US</a><a>BLOG</a>
  </nav>
</header>

<div class="abs hero-photo" role="img" aria-label="Tiered white wedding cake with pink roses, bride and groom cutting it, under a rose tint"></div>
<svg class="abs hero-wave" viewBox="0 0 1200 140" preserveAspectRatio="none">
  <path d="M0 70 Q600 160 1200 20 L1200 140 L0 140 Z" fill="#fff"/>
  <path d="M0 70 Q600 160 1200 20" fill="none" stroke="#c8566a" stroke-width="6"/>
</svg>

<form class="abs signup-card">
  <span class="flower" role="img" aria-label="Pink rose decoration"></span>
  <h3>Create Your Account</h3>
  <label>First Name</label><div class="field">@example</div>
  <label>Last Name</label><div class="field">@example</div>
  <label>Email</label><div class="field">youremail@example.com</div>
  <label>Password</label><div class="field">@example</div>
  <div class="btn btn-rose">Create Now</div>
</form>

<div class="abs press" aria-label="As featured in">
  <span></span><span></span><span></span><span></span><span></span><span></span><span></span>
</div>

<div class="abs floral-right" role="img" aria-label="Watercolour pink and white roses"></div>
<div class="abs floral-left" role="img" aria-label="Watercolour pink and white roses"></div>

<div class="abs video" role="img" aria-label="Video still of a whiteboard presentation, pink tint">
  <div class="video-title">Watch This First Click Here</div>
  <svg class="video-play" viewBox="0 0 52 52"><circle cx="26" cy="26" r="24" fill="none" stroke="#fff" stroke-width="2"/><path d="M21 16 L36 26 L21 36 Z" fill="#fff"/></svg>
  <div class="video-bar"><i></i><b></b></div>
</div>
<form class="abs discover">
  <h3>How a New Discovery Sells More Wedding Cakes and at Higher Prices!</h3>
  <div class="input">Your First Name</div>
  <div class="input">Your Last Name</div>
  <div class="input">Your Email</div>
  <div class="btn btn-rose">Watch Now</div>
</form>

<h2 class="abs section-title" style="top:1192px">MARKETING SOLUTIONS</h2>
<p class="abs section-sub" style="top:1228px">Our research is not just a game changer. It is the game changer. We're rewriting the book for selling wedding cakes</p>
<div class="abs market-cards">
  <div class="market-card"><p>I'm New to Selling Wedding Cakes…</p><div class="btn btn-grey">Click Here</div></div>
  <div class="market-card"><p>I Want to Maintain My Sales…</p><div class="btn btn-rose">Click Here</div></div>
  <div class="market-card"><p>I'm Eager to Boost My Sales and Profits…</p><div class="btn btn-grey">Click Here</div></div>
  <div class="market-card"><p>I'm Ready to Dominate My Market Area…</p><div class="btn btn-grey">Click Here</div></div>
</div>

<h2 class="abs section-title" style="top:1462px">SALES SOLUTIONS</h2>
<p class="abs section-sub" style="top:1498px">Lorem ipsum dolor sit amet, consectetur adipiscing elit. Etiam voluptatem. Inquit, Epicurus ignoral</p>
<div class="abs sales-cards">
  <div class="sales-card"><div class="photo" role="img" aria-label="Three pastry chefs holding a book" style="background:linear-gradient(135deg,#f2f2f2,#9a8888)"></div><p>Become the "World's Greatest." You'll have an atmosphere so special, brides won't think of using anyone but you!</p><div class="btn btn-grey">Read More</div></div>
  <div class="sales-card"><div class="photo" role="img" aria-label="Puzzled woman in front of a chalkboard question mark" style="background:linear-gradient(135deg,#5a4a48,#2c2c2c)"></div><p>Peek at a very effective psychological sales riddle called "The Insecurity Gap."</p><div class="btn btn-grey">Read More</div></div>
  <div class="sales-card"><div class="photo" role="img" aria-label="Split portrait showing two sides of one person" style="background:linear-gradient(90deg,#e8d0b8,#d8d8d8)"></div><p>Discover a sales growth secret that reveals the "Two Faces of Your Wedding Cake Business."</p><div class="btn btn-grey">Read More</div></div>
</div>

<svg class="abs founder-band" viewBox="0 0 1200 512" preserveAspectRatio="none">
  <path d="M0 70 Q500 130 1200 10 L1200 512 L0 512 Z" fill="#f1d3d8"/>
  <path d="M0 70 Q500 130 1200 10" fill="none" stroke="#c8566a" stroke-width="6"/>
</svg>
<div class="abs founder-photo" role="img" aria-label="Portrait of the founder in a patterned shirt">
  <div class="founder-ribbon">Ray Dalton</div>
</div>
<div class="abs founder-copy">
  <h2>Use Cutting-edge Methods Proven to Generate MORE Leads, Convince MORE Brides to Choose You, Get HIGHER Prices and DOMINATE Your Competition.</h2>
  <p>Our breakthrough marketing and sales methods are possible due to the long-term research studies we've conducted with 150,000 brides over the past 12 years.</p>
  <p>From the findings, we have developed new and revolutionary marketing strategies, sales tools, and a complete transformational wedding cake sales system. But, don't take my word for it…let me "prove" the value and impact they will have on your wedding cake business.</p>
</div>

<div class="abs advisory-copy">
  <p>Enter Your Name and Email Address Below. Each month you'll receive our "Advanced Wedding Cake Marketing Advisory." It's normally available for a $397 subscription fee. You'll receive the first year… absolutely FREE.</p>
  <p>Join our <em>"Insider Advisory"</em> for FREE." You'll receive the latest research secrets while learning how to use psychology for gaining a decisive advantage to market and sell your wedding cakes.</p>
</div>
<form class="abs advisory-form">
  <div class="input">Your First Name</div>
  <div class="input">Your Last Name</div>
  <div class="input">Your Email</div>
  <div class="btn btn-rose">Join With Us</div>
  <small>We dislike spam as much as you do. Therefore, we'll never sell, rent, or give away your email address.</small>
</form>

<footer class="abs site-footer">
  <div class="footer-col" style="left:244px"><h4>Marketing Solutions</h4><ul>
    <li>Cracking the Secret Code Course</li><li>Individual Marketing Videos</li><li>Bundled Marketing Videos</li><li>Gold Standard Baker</li><li>Advertise For Free</li><li>Analyze Your Marketing</li><li>Master Hierarchy Training</li></ul></div>
  <div class="footer-col" style="left:442px"><h4>Sales Solutions</h4><ul>
    <li>Individual Sales Tools</li><li>Bundles Sales Presentations</li><li>Advanced Insider Bulletin</li><li>Write a Wedding Cake Book</li><li>Analyze Your Sales System</li></ul></div>
  <div class="footer-col" style="left:614px"><h4>Hire Us</h4><ul>
    <li>Coaching</li><li>Consulting</li><li>Speaking</li><li>3-Day Workshops</li></ul></div>
  <div class="footer-col" style="left:736px"><h4>Partner With Us</h4><ul><li>Spread the Word</li></ul></div>
  <div class="footer-col" style="left:860px"><h4>Recent Blog Posts</h4></div>
  <p class="copyright">© 2018 Northfield Pastry Trade Institute. Trademarks and brands are the property of their respective owners.</p>
</footer>

</body>
</html>
```